Medical Call Centre Needs a Web Design

We need a web design for a new company based in Melbourne called "Clinora Services". We provide medical centres with administrative support by managing inbound calls to our clients facility. We require a clean, simple and easy to navigate website with an ultimate end product alike this - http://www.plumevanta.com/

The final design should communicate professionalism, new age and inovative.

Industry/Entity Type

It Company

```html
<!DOCTYPE html>
<html lang="en">
<head>
<meta charset="utf-8">
<title>Clinora Services</title>
<link rel="stylesheet" href="https://fonts.googleapis.com/css2?family=Montserrat:wght@400;500;600&family=Mulish:ital,wght@0,400;0,600;1,400&display=swap">
<style>
:root{
  --bg:#f0c13b;
  --bg-line:#f7dc8a;
  --red:#c8102e;
  --ink:#5b4713;
  --button:#d7a52b;
  --white:#ffffff;
  --frame:#f6e6b8;
}
*{margin:0;padding:0;box-sizing:border-box}
html,body{width:673px;height:1200px;overflow:hidden}
body{background:var(--bg);font-family:"Mulish",sans-serif;color:var(--ink);position:relative}
.abs{position:absolute}
.top-nav{left:0;top:0;width:673px;height:32px;border-bottom:1px solid var(--bg-line)}
.top-nav ul{list-style:none;display:flex;gap:20px;position:absolute;left:42px;top:12px}
.top-nav li{font:500 8px "Montserrat",sans-serif;color:var(--white);letter-spacing:.2px}
.account{right:42px;top:12px;font:600 6.5px "Montserrat",sans-serif;color:var(--white)}
.account .sep{color:var(--red);margin:0 3px}
.account .signup{color:var(--red)}
.logo{left:41px;top:38px;width:62px;height:62px;border-radius:50%;border:1px solid var(--bg-line);background:var(--bg)}
.logo span{position:absolute;left:8px;top:14px;font:600 10px/11px "Montserrat",sans-serif;color:var(--white)}
.label{font:500 8px "Montserrat",sans-serif;color:var(--red)}
.phone{left:476px;top:66px;font:400 11px "Montserrat",sans-serif;color:var(--white)}
.vsep{left:558px;top:48px;width:1px;height:36px;background:var(--bg-line)}
.social{left:558px;top:64px;display:flex;gap:4px}
.social i{width:15px;height:15px;border-radius:50%;background:var(--white);display:block}
.hero{left:42px;top:107px;width:589px;height:223px;border:2px solid var(--frame);background:linear-gradient(90deg,#d9dbe0 0%,#e9e7e6 40%,#d8b9a6 65%,#bda190 100%)}
.hero p{position:absolute;left:19px;top:67px;width:260px;font:400 15.5px/19.5px "Montserrat",sans-serif;color:var(--red)}
.dots{left:63px;top:268px;display:flex;gap:3px}
.dots i{width:6px;height:6px;border-radius:50%;background:var(--white);display:block}
.dots i:first-child{background:var(--bg)}
.heading{font:400 13px "Montserrat",sans-serif;color:var(--red);white-space:nowrap}
.divider{left:0;width:673px;height:16px;overflow:visible}
.copy{font-size:7.1px;line-height:12.4px}
.photo{border:2px solid var(--frame)}
.btn{width:72px;height:21px;background:var(--button);color:var(--white);font:500 6.5px/21px "Montserrat",sans-serif;text-align:center}
.clients{left:42px;top:851px;width:590px;display:flex;justify-content:space-between;font:600 10px "Mulish",sans-serif;color:var(--white)}
.news{width:190px}
.news .date{font:500 7px "Montserrat",sans-serif;color:#3a2d08;margin-bottom:3px}
.news .more{color:var(--red);font-size:7px;margin-top:7px}
.quote{left:142px;top:1049px;width:490px;font-style:italic}
.quote-mark{display:inline-block;width:13px;height:9px;border-radius:4px;background:var(--white);vertical-align:middle;margin-right:4px}
.author{left:142px;top:1104px;font-size:7px;color:var(--red)}
.footer-line{left:0;top:1138px;width:673px;height:1px;background:var(--bg-line)}
.footer{left:0;top:1158px;width:673px;text-align:center;font-size:5.8px;line-height:10px;color:var(--white)}
.footer span{color:var(--ink)}
</style>
</head>
<body>

<nav class="abs top-nav">
  <ul><li>HOME</li><li>ABOUT US</li><li>OUR SERVICES</li><li>CLIENTS</li><li>NEWS</li><li>BLOG</li><li>CONTACT US</li></ul>
</nav>
<div class="abs account">LOG IN<span class="sep">|</span><span class="signup">SIGN UP</span></div>

<div class="abs logo"><span>Clinora<br>Services</span></div>

<div class="abs label" style="left:476px;top:49px">Call Us:</div>
<div class="abs phone">140 555 2718</div>
<div class="abs vsep"></div>
<div class="abs label" style="left:558px;top:47px">Connect Us:</div>
<div class="abs social"><i></i><i></i><i></i><i></i></div>

<section class="abs hero" role="img" aria-label="Photo of smiling call centre agents wearing headsets">
  <p>We provide medical centres with administrative support by managing inbound calls to our clients facility.</p>
</section>
<div class="abs dots"><i></i><i></i><i></i><i></i></div>

<!-- Welcome -->
<svg class="abs divider" style="top:362px" viewBox="0 0 673 16"><polyline points="42,6 80,6 88,14 96,6 445,6" fill="none" stroke="#f7dc8a" stroke-width="1"/></svg>
<h2 class="abs heading" style="right:41px;top:360px">WELCOME TO OUR WEBSITE</h2>
<div class="abs photo" style="left:42px;top:393px;width:236px;height:129px;background:linear-gradient(180deg,#f2f2f2,#dfe4e8 70%,#9fb6c8)" role="img" aria-label="Photo of a smiling medical team in white coats"></div>
<p class="abs copy" style="left:294px;top:390px;width:336px">Aliquam molestie, mi et imperdiet euismod, dui purus auctor tellus, et interdum lacus lectus et ante. Sed accumsan sollicitudin sapien, sit amet adipiscing turpis gravida ac. In congue, neque ac lobortis volutpat, libero mauris varius mi, vitae suscipit ipsum ligula vitae risus. Duis aliquam nibh a dui iaculis viverra id a velit. Vivamus egestas risus in magna varius commodo. Sed semper viverra egestas. Etiam pretium porttitor lectus, vel ornare neque porta volutpat. Ut et scelerisque ante. Donec erat purus, faucibus vitae congue vel, porttitor nec lectus. Aenean a nibh eget turpis vehicula tempus ac sed massa. Vestibulum dolor nulla, ultrices ac tincidunt sed, laoreet non est. Suspendisse lobortis turpis in odio blandit ac interdum lorem euismod...</p>
<div class="abs btn" style="left:294px;top:502px">READ MORE ››</div>

<!-- What we do -->
<h2 class="abs heading" style="left:42px;top:550px">WHAT WE DO</h2>
<svg class="abs divider" style="top:552px" viewBox="0 0 673 16"><polyline points="140,6 576,6 584,14 592,6 632,6" fill="none" stroke="#f7dc8a" stroke-width="1"/></svg>
<p class="abs copy" style="left:42px;top:579px;width:334px">Aliquam molestie, mi et imperdiet euismod, dui purus auctor tellus, et interdum lacus lectus et ante. Sed accumsan sollicitudin sapien, sit amet adipiscing turpis gravida ac. In congue, neque ac lobortis volutpat, libero mauris varius mi, vitae suscipit ipsum ligula vitae risus. Duis aliquam nibh a dui iaculis viverra id a velit. Vivamus egestas risus in magna varius commodo. Sed semper viverra egestas. Etiam pretium porttitor lectus, vel ornare neque porta volutpat. Ut et scelerisque ante. Donec erat purus, faucibus vitae congue vel, porttitor nec lectus. Aenean a nibh eget turpis vehicula tempus ac sed massa. Vestibulum dolor nulla, ultrices ac tincidunt sed, laoreet non est. Suspendisse lobortis turpis in odio blandit ac interdum lorem euismod...</p>
<div class="abs btn" style="left:42px;top:691px">READ MORE ››</div>
<div class="abs photo" style="left:395px;top:582px;width:111px;height:67px;background:linear-gradient(135deg,#e8e8e6,#c9c2ba)" role="img" aria-label="Photo of two agents with headsets at computers"></div>
<div class="abs photo" style="left:522px;top:582px;width:110px;height:67px;background:linear-gradient(135deg,#6d6a5e,#b98a6e 50%,#7e9b6a)" role="img" aria-label="Photo of an agent with a headset by a window"></div>
<div class="abs photo" style="left:395px;top:658px;width:111px;height:67px;background:linear-gradient(135deg,#eef0f2,#c7cdd3)" role="img" aria-label="Photo of a doctor with colleagues in a meeting"></div>
<div class="abs photo" style="left:522px;top:658px;width:110px;height:67px;background:linear-gradient(135deg,#f3f3f3,#d5d6d8)" role="img" aria-label="Photo of hands typing on a laptop"></div>

<!-- Clients -->
<svg class="abs divider" style="top:759px" viewBox="0 0 673 16"><polyline points="42,6 80,6 88,14 96,6 530,6" fill="none" stroke="#f7dc8a" stroke-width="1"/></svg>
<h2 class="abs heading" style="right:41px;top:757px">OUR CLIENTS</h2>
<p class="abs copy" style="left:42px;top:796px;width:592px">Aliquam molestie, mi et imperdiet euismod, dui purus auctor tellus, et interdum lacus lectus et ante. Sed accumsan sollicitudin sapien, sit amet adipiscing turpis gravida ac. In congue, neque ac lobortis volutpat, libero mauris varius mi, vitae suscipit ipsum ligula vitae risus. Duis aliquam nibh a dui iaculis viverra id a velit. Vivamus egestas risus in magna varius commodo. Sed semper viverra egestas.</p>
<div class="abs clients"><span>Harvella</span><span>Quorin</span><span>Netlyra</span><span>Pellum</span><span>Zentrax</span><span>Olvo</span><span>Brightcore</span><span>Axen</span><span>Corvane</span><span>Lumeo</span><span>Veyra</span></div>

<!-- News -->
<h2 class="abs heading" style="left:42px;top:884px">LATEST NEWS</h2>
<svg class="abs divider" style="top:886px" viewBox="0 0 673 16"><polyline points="140,6 576,6 584,14 592,6 632,6" fill="none" stroke="#f7dc8a" stroke-width="1"/></svg>
<div class="abs news" style="left:42px;top:917px"><div class="date">JULY 01, 2014</div><p class="copy">Aliquam molestie, mi et imperdiet euismod, dui purus auctor tellus, et interdum lacus lectus et ante. Sed accumsan sollicitudin sapien, sit amet adipiscing turpis gravida ac. In congue, neque ac lobortis....</p><div class="more">Read More ››</div></div>
<div class="abs news" style="left:243px;top:917px"><div class="date">JULY 01, 2014</div><p class="copy">Aliquam molestie, mi et imperdiet euismod, dui purus auctor tellus, et interdum lacus lectus et ante. Sed accumsan sollicitudin sapien, sit amet adipiscing turpis gravida ac. In congue, neque ac lobortis....</p><div class="more">Read More ››</div></div>
<div class="abs news" style="left:446px;top:917px"><div class="date">JULY 01, 2014</div><p class="copy">Aliquam molestie, mi et imperdiet euismod, dui purus auctor tellus, et interdum lacus lectus et ante. Sed accumsan sollicitudin sapien, sit amet adipiscing turpis gravida ac. In congue, neque ac lobortis....</p><div class="more">Read More ››</div></div>

<!-- Testimonials -->
<svg class="abs divider" style="top:1016px" viewBox="0 0 673 16"><polyline points="42,6 80,6 88,14 96,6 515,6" fill="none" stroke="#f7dc8a" stroke-width="1"/></svg>
<h2 class="abs heading" style="right:41px;top:1014px">TESTIMONIALS</h2>
<div class="abs photo" style="left:42px;top:1050px;width:85px;height:64px;background:linear-gradient(135deg,#e7ecef,#b9c3cb)" role="img" aria-label="Portrait photo of a smiling client"></div>
<p class="abs copy quote"><span class="quote-mark"></span>Aliquam molestie, mi et imperdiet euismod, dui purus auctor tellus, et interdum lacus lectus et ante. Sed accumsan sollicitudin sapien, sit amet adipiscing turpis gravida ac. In congue, neque ac lobortis volutpat, libero mauris varius mi, vitae suscipit ipsum ligula vitae risus. Duis aliquam nibh a dui iaculis viverra id a velit. Vivamus egestas risus in magna varius commodo. Sed semper viverra egestas. Etiam pretium porttitor lectus, vel ornare neque porta volutpat. Ut et scelerisque ante....</p>
<div class="abs author">-Daniel Rowe</div>

<div class="abs footer-line"></div>
<footer class="abs footer">Copyright © 2014 <span>Company Name</span><br>All Right Reserved</footer>

</body>
</html>
```